依頼概要
■依頼の目的/概要
・弊社は葬儀社と仏壇店舗を運営しており、当社会員様・提携先会員様向けのお盆売 り出しの案内DM(郵送DM A4サイズ片面カラー)の作成をお願いします。

・ラフスケッチ・ロゴ、写真、施設の写真等の素材はご用意しています。

・開封率を上げたいのと、年配層に受け入れやすいように『手書き』もしくは、『手書きテイスト』での作成をお願いします。

・A4サイズを三つ折りにして、透明封筒に入れて発送する予定です。

・右上に『料金別納郵便』の表記は必ず入れて下さい(昨年DM参考資料あり)

■依頼詳細
デザイン案:添付ファイル参照
枚数:2,000枚
サイズ:A4、片面

・開封率を上げたいのと、年配層に受け入れやすいように『手書き』『手書きテイス ト』での作成をお願いします。

■要望点
・上記のとおり、デザイン等は添付ファイルのものを仕様して頂きます。

・納品ファイル;イラストレータ形式(ai)
高解像度JPEG
PDF

・最終的にはネット印刷に入稿しますので、当社指定のネット印刷会社のフォーマットに合うように納品して下さい。
アウトライン化したものと、アウトライン化していないもの、両方のデータを納品してください。
また、こちらで微調整をする可能性がありますので、編集しやすいようにaiファイル内を整理しておいていただけると助かります。

その他何かご不明な点がございましたら、お気軽にご質問下さい。
よろしくお願いいたします。

※添付ファイル以外にデータまだあります

```html
<!DOCTYPE html>
<html lang="ja">
<head>
<meta charset="utf-8">
<title>お盆特選販売会 案内</title>
<link href="https://fonts.googleapis.com/css2?family=Klee+One:wght@400;600&family=Yusei+Magic&family=Mochiy+Pop+One&display=swap" rel="stylesheet">
<style>
:root{
  --red:#d7262c;
  --red-dark:#b3161c;
  --pink:#f6d9d6;
  --cream:#fffaf0;
  --yellow:#ffe14a;
  --ink:#2b2420;
  --grey:#6c6460;
  --line:#e3c9c4;
}
*{box-sizing:border-box;margin:0;padding:0}
html,body{width:849px;height:1200px;overflow:hidden;background:#fff}
body{font-family:"Klee One",serif;color:var(--ink)}
.sheet{position:relative;width:849px;height:1200px;background:var(--cream);overflow:hidden}
.abs{position:absolute}
.photo{position:absolute;border-radius:4px}

/* header */
.sale-kicker{left:30px;top:10px;font-size:44px;color:var(--red);font-family:"Yusei Magic",sans-serif;letter-spacing:2px;line-height:1.1;white-space:nowrap}
.sale-kicker small{font-size:28px}
.sale-period{left:125px;top:58px;background:var(--red);color:#fff;font-size:17px;padding:1px 10px;border-radius:3px;font-family:"Yusei Magic",sans-serif;white-space:nowrap}
.items{left:30px;top:88px;font-size:20px;color:var(--red);font-family:"Yusei Magic",sans-serif;line-height:1.3;white-space:nowrap}
.half{left:70px;top:118px;font-family:"Mochiy Pop One",sans-serif;font-size:136px;color:var(--red);letter-spacing:8px;line-height:1}
.half-ring{left:40px;top:102px;width:380px;height:180px}
.discount{left:240px;top:268px;font-size:26px;color:var(--red);font-family:"Yusei Magic",sans-serif}
.present{left:110px;top:298px;font-size:28px;color:var(--red);font-family:"Yusei Magic",sans-serif;white-space:nowrap}
.present-note{left:130px;top:337px;background:var(--red);color:#fff;font-size:14px;padding:1px 12px;border-radius:12px;white-space:nowrap}

.postage{right:14px;top:12px;width:92px;height:56px;border:2px solid var(--ink);font-size:15px;text-align:center;line-height:1.25;padding-top:6px;background:#fff}
.catalog-note{left:475px;top:204px;font-size:15px;line-height:1.4;color:var(--ink)}
.company{left:555px;top:274px;display:flex;align-items:center;gap:6px;font-size:19px;font-weight:600;white-space:nowrap}
.company i{display:block;width:22px;height:22px;background:var(--red);border-radius:50%}
.phone{left:555px;top:302px;display:flex;align-items:center;gap:6px;font-size:26px;font-weight:600;color:var(--red);white-space:nowrap;line-height:1.2}
.addr{left:555px;top:340px;font-size:10px;color:var(--grey);line-height:1.3;white-space:nowrap}

/* news band */
.news-band{left:0;top:368px;width:849px;height:30px;background:var(--pink)}
.news-title{left:0;top:370px;width:849px;text-align:center;font-size:21px;color:var(--red-dark);font-family:"Yusei Magic",sans-serif}
.news-title small{font-size:10px;color:var(--grey)}

.rank{display:inline-flex;align-items:center;justify-content:center;flex:none;width:40px;height:40px;border-radius:50%;background:var(--yellow);color:var(--red);font-family:"Yusei Magic",sans-serif;font-size:15px}
.news-head{font-size:19px;line-height:1.35;color:var(--ink);font-family:"Yusei Magic",sans-serif}
.news-head em{font-style:normal;color:var(--red)}
.body{font-size:12px;line-height:1.5;color:var(--ink)}

.info-box{left:20px;top:722px;width:425px;font-size:18px;line-height:1.55;color:var(--red-dark);font-family:"Yusei Magic",sans-serif}
.info-box p{border-bottom:1px dashed var(--line);white-space:nowrap}

.lantern-label{left:640px;top:640px;width:130px;height:120px;background:var(--red);color:#fff;font-family:"Yusei Magic",sans-serif;font-size:17px;text-align:center;padding-top:18px;line-height:1.35}
.lantern-label b{font-size:28px;font-weight:400}

/* footer */
.foot{left:0;top:1088px;width:849px;height:112px;background:var(--pink)}
.foot-tag{left:14px;top:1098px;background:var(--yellow);color:var(--red);font-family:"Yusei Magic",sans-serif;font-size:17px;padding:6px 12px;line-height:1.25;border-radius:4px;white-space:nowrap}
.foot-tag b{font-size:24px;font-weight:400}
.foot-msg{left:455px;top:1108px;width:385px;font-size:14px;line-height:1.8;color:var(--ink);white-space:nowrap}
.foot-msg b{color:var(--red);font-size:26px;font-weight:600}
</style>
</head>
<body>
<main class="sheet">

  <div class="abs sale-kicker">お盆<small>特選販売会</small></div>
  <div class="abs sale-period">本日〜8月16日</div>
  <div class="abs items">ちょうちん・お線香・お仏壇・仏具が</div>
  <svg class="abs half-ring" viewBox="0 0 380 180" aria-hidden="true">
    <ellipse cx="190" cy="92" rx="180" ry="80" fill="none" stroke="#d7262c" stroke-width="3"/>
  </svg>
  <div class="abs half">半額</div>
  <div class="abs discount">〜10%OFF</div>
  <div class="abs present">ご来店プレゼントあり！</div>
  <div class="abs present-note">詳しくは最後をご覧下さい</div>

  <div class="abs postage">料金別納<br>郵便</div>
  <div class="photo" style="left:470px;top:14px;width:120px;height:180px;background:linear-gradient(160deg,#e9e1d4,#bfb09a)" role="img" aria-label="店舗外観の写真"></div>
  <div class="photo" style="left:598px;top:78px;width:130px;height:120px;background:linear-gradient(160deg,#d4dde6,#a7b4c1)" role="img" aria-label="葬儀会館の写真"></div>
  <div class="photo" style="left:735px;top:78px;width:100px;height:120px;background:linear-gradient(160deg,#f0d7c7,#d9a98c)" role="img" aria-label="お盆用カタログチラシの写真"></div>
  <div class="abs catalog-note">お盆用の<br>カタログチラシを<br>同封しています。</div>
  <div class="abs company"><i></i>株式会社みどり野葬儀社</div>
  <div class="abs phone">☎ 022-000-1234</div>
  <div class="abs addr">〒000-0000 宮城県○○市中央町1丁目2番3号</div>

  <div class="abs news-band"></div>
  <div class="abs news-title">今年1年間の「みどり野葬儀社」ニュース ベスト3 <small>2024.8〜2025.7</small></div>

  <div class="abs" style="left:18px;top:408px;display:flex;gap:8px;width:420px">
    <span class="rank">第1位</span>
    <p class="news-head">ひかりホール西町がリニューアルで<br><em>わぁステキ！</em>の声がたくさん！</p>
  </div>
  <div class="photo" style="left:20px;top:470px;width:190px;height:130px;background:linear-gradient(160deg,#d9cdb8,#a6937a)" role="img" aria-label="リニューアルした葬儀式場の写真"></div>
  <div class="abs body" style="left:220px;top:470px;width:220px">人気の家族葬に合う式場を新たにご用意。明るく落ち着いた空間で、ゆっくりとお別れの時間をお過ごしいただけます。</div>
  <div class="photo" style="left:20px;top:608px;width:145px;height:100px;background:linear-gradient(160deg,#e6e0d8,#b9ada0)" role="img" aria-label="ベッドルームの写真"></div>
  <div class="photo" style="left:172px;top:608px;width:130px;height:100px;background:linear-gradient(160deg,#d8e0e6,#9fb0bd)" role="img" aria-label="お風呂の写真"></div>
  <div class="photo" style="left:310px;top:608px;width:130px;height:100px;background:linear-gradient(160deg,#e8d9c6,#c3a887)" role="img" aria-label="控室の写真"></div>

  <div class="abs" style="left:465px;top:408px;display:flex;gap:8px;width:370px">
    <span class="rank">第2位</span>
    <p class="news-head">贈答用のお線香とお盆ちょうちんが<br><em>大人気！</em>品切れが続出しました。</p>
  </div>
  <div class="abs body" style="left:465px;top:470px;width:200px">昨年のお盆は贈答用のお線香が大変好評でした。今年は品数を増やしてご用意しております。</div>
  <div class="photo" style="left:675px;top:465px;width:160px;height:110px;background:linear-gradient(160deg,#eadbe8,#b89ab3)" role="img" aria-label="贈答用お線香の写真"></div>

  <div class="abs" style="left:465px;top:585px;display:flex;gap:8px;width:200px">
    <span class="rank">第3位</span>
    <p class="news-head" style="font-size:16px">「みなと鎮魂の日」<br>追悼式典をお手伝い</p>
  </div>
  <div class="abs body" style="left:465px;top:632px;width:165px">地域の皆様と共に祈りを捧げる式典の設営と運営をお手伝いいたしました。</div>

  <div class="abs info-box">
    <p>会員様は、いつでも見学が出来ます！</p>
    <p>おいしいお茶とお菓子をご用意してお待ちしています。</p>
    <p>もちろん葬儀に関してもお気軽にご相談下さい。</p>
  </div>

  <div class="photo" style="left:20px;top:830px;width:425px;height:250px;background:linear-gradient(160deg,#e4d3b9,#b08e63)" role="img" aria-label="仏壇と仏具の店内展示の写真"></div>

  <div class="photo" style="left:465px;top:700px;width:370px;height:380px;background:linear-gradient(170deg,#f0e4cf,#d4a66d 60%,#8d5a32)" role="img" aria-label="お盆提灯の写真"></div>
  <div class="abs lantern-label">地域特別の<br>品揃え<br><b>お盆提灯</b></div>

  <div class="abs foot"></div>
  <div class="abs foot-tag">お盆特選販売会<br><b>ご来店プレゼント</b></div>
  <div class="photo" style="left:230px;top:1096px;width:210px;height:96px;background:linear-gradient(160deg,#e7d8c4,#b29273)" role="img" aria-label="プレゼントのお線香の写真"></div>
  <div class="abs foot-msg">こちらのチラシご持参で<br>お好きなご線香をそれぞれで <b>3点</b> プレゼントします。</div>

</main>
</body>
</html>
```